Business Cards - Both Co-Branded and Single Branded

We need a new business card design with a few versions. We need shells and imprints. Old designs are loaded, as well as our logos. The new business card design should be a fold over card since there is so much information.

Versions:
1. Single brand - Keystone Coverage Partners Logo version
2. Co-Branded - Keystone Coverage Partners Logo AND Brightwater's logo (Both logos must appear to be the same size, they have to appear equal vs one more dominant than the other)

Our corporate colors are PMS #2727 and #877 (Silver) - please use these in the shell.

Our traditional fonts are Trajan Pro (in all caps or all lowercase, not both), and Futura LT BT Light

I have included PDFs of our current card to give you an idea of how much info needs to go on the cards, as well as some common info that can be incorporated into the shells.

Target Market(s)

Schools, Cities and County Employers in the US

Industry/Entity Type

Insurance

Contact Information for Business Card

We want a fold over card. Prefer no rounded corners - as we had that on our last card. Fold can be either vertical or horizontal. It could also be a short fold if your design supports that.

Font styles to use
Other font styles liked:
• Futura LT BT Light and Trajan Pro can be used

Requirements
Must have
• Must be designed in InDesign so all artwork can be turned over to our printer.
• Our copyright line (as seen on the samples of our current card)
• We have some reps with a lot of information on the their imprint, including insurance licensing information, designations etc - please keep this in mind when spacing things out. (See PDF "KCP New Nock Up..") - the "ARBT" PPACA logo is now available in our uploaded files.
• IMPRINT SECTION: Must be on top of white background - we need the imprint portion to be an economical option - as the printer will pre-print the shells. Sections for employee info, the imprint, must be in black or a variation of black (no lower than 85% black) as this will serve as our one color imprint.
Should not have
• No imprint color over another color (example, silver over blue or silver over black) Also no Multiple colors in the imprint.

```html
<!DOCTYPE html>
<html lang="en">
<head>
<meta charset="utf-8">
<title>Keystone Coverage Partners – Business Card</title>
<link rel="stylesheet" href="https://fonts.googleapis.com/css2?family=Cinzel:wght@400&family=Jost:ital,wght@0,400;0,700;1,400&family=Arimo:wght@700&display=swap">
<style>
  :root {
    --backdrop: #ebeceb;
    --card: #ffffff;
    --brand-blue: #4877d6;
    --ink: #555555;
    --ink-dark: #444444;
    --silver: #8a8d90;
    --map-tone: #f4f7fd;
    --edge: #d4d4d4;
  }
  * { margin: 0; padding: 0; box-sizing: border-box; }
  html, body { width: 1126px; height: 1200px; overflow: hidden; }
  body { background: var(--backdrop); position: relative; font-family: "Jost", sans-serif; color: var(--ink); }

  .card { position: absolute; left: 172px; width: 696px; height: 397px; background: var(--card); }
  .card-front { top: 173px; box-shadow: 6px 8px 14px rgba(0,0,0,0.25); }
  .card-back { top: 590px; border: 1px solid var(--edge); overflow: hidden; }

  .wordmark {
    position: absolute; top: 42px; left: 0; width: 100%; text-align: center;
    font-family: "Cinzel", serif; font-size: 31px; letter-spacing: 1px; color: var(--silver);
  }

  .holder { position: absolute; right: 446px; top: 183px; text-align: right; }
  .holder-name { font-weight: 700; font-size: 28px; color: var(--ink); line-height: 1; letter-spacing: 0.5px; }
  .holder-role { font-style: italic; font-size: 20px; line-height: 25px; margin-top: 14px; color: var(--ink); }

  .divider { position: absolute; left: 261px; top: 150px; width: 3px; height: 184px; background: var(--brand-blue); }

  .contact-list { position: absolute; left: 276px; top: 143px; list-style: none; }
  .contact-item { display: flex; align-items: center; font-size: 25px; height: 31px; color: var(--ink); }
  .contact-item svg { width: 22px; height: 22px; margin-right: 9px; flex: none; }
  .contact-item.fax { margin-top: 3px; }
  .contact-item.address { align-items: flex-start; font-size: 21px; line-height: 25px; height: auto; margin-top: 13px; }
  .contact-item.address svg { margin-top: 12px; margin-right: 7px; }

  .news-panel { position: absolute; left: 0; top: 0; width: 346px; height: 100%; background: var(--brand-blue); }
  .panel-rule { position: absolute; left: 353px; top: 0; width: 5px; height: 100%; background: var(--brand-blue); }
  .map-art { position: absolute; left: 43px; top: 82px; width: 270px; height: 160px; background: var(--map-tone); border-radius: 10px 30px 40px 20px; }
  .news-title { position: absolute; left: 0; width: 100%; top: 269px; text-align: center; font-family: "Arimo", sans-serif; font-weight: 700; color: #fff; font-size: 20px; }
  .news-url { position: absolute; left: 0; width: 100%; top: 295px; text-align: center; font-family: "Arimo", sans-serif; font-weight: 700; color: #fff; font-size: 22px; }

  .social { position: absolute; left: 392px; top: 134px; display: flex; align-items: center; }
  .social-dot { width: 38px; height: 38px; border-radius: 50%; background: var(--brand-blue); flex: none; }
  .social-text { margin-left: 12px; text-align: center; font-size: 19px; line-height: 24px; color: var(--ink-dark); }
  .tollfree { position: absolute; left: 358px; width: 338px; top: 194px; text-align: center; color: var(--ink-dark); }
  .tollfree-label { font-size: 28px; line-height: 34px; }
  .tollfree-number { font-size: 31px; font-weight: 700; line-height: 38px; }
</style>
</head>
<body>
  <section class="card card-front">
    <div class="wordmark">KEYSTONE COVERAGE PARTNERS</div>

    <div class="holder">
      <div class="holder-name">Laura Penning</div>
      <div class="holder-role">Account Representative<br>PPACA Certified</div>
    </div>

    <div class="divider"></div>

    <ul class="contact-list">
      <li class="contact-item email">
        <svg viewBox="0 0 24 24" fill="none" stroke="var(--brand-blue)" stroke-width="2"><rect x="2" y="5" width="20" height="14"/><path d="M2 5l10 8 10-8"/></svg>
        lpenning@KCPBenefits.com
      </li>
      <li class="contact-item phone">
        <svg viewBox="0 0 24 24" fill="var(--brand-blue)"><path d="M6.6 2.5l3 .6 1 4.4-2.2 1.6a12 12 0 006.5 6.5l1.6-2.2 4.4 1 .6 3-2 2.6C11 19.5 4.5 13 3.9 4.5z"/></svg>
        555.210.4418
      </li>
      <li class="contact-item mobile">
        <svg viewBox="0 0 24 24" fill="none" stroke="var(--brand-blue)" stroke-width="2"><rect x="5" y="2" width="14" height="20" rx="2"/><line x1="10" y1="18" x2="14" y2="18"/></svg>
        555.733.0926
      </li>
      <li class="contact-item fax">
        <svg viewBox="0 0 24 24" fill="var(--brand-blue)"><rect x="6" y="2" width="12" height="6"/><rect x="2" y="9" width="20" height="9" rx="2"/><rect x="6" y="14" width="12" height="8" fill="#fff" stroke="var(--brand-blue)" stroke-width="2"/></svg>
        555.210.4419
      </li>
      <li class="contact-item address">
        <svg viewBox="0 0 24 24" fill="var(--brand-blue)"><path d="M12 1a7 7 0 00-7 7c0 5 7 15 7 15s7-10 7-15a7 7 0 00-7-7zm0 10a3 3 0 110-6 3 3 0 010 6z"/></svg>
        <span>2270 Maple Ridge Road, Suite 310<br>Cedar Falls, MN 55012</span>
      </li>
    </ul>
  </section>

  <section class="card card-back">
    <div class="news-panel">
      <div class="map-art" role="img" aria-label="United States map filled with flag stripes and a star"></div>
      <div class="news-title">Public Sector News</div>
      <div class="news-url">www.KCPBenefits.com/news</div>
    </div>
    <div class="panel-rule"></div>

    <div class="social">
      <div class="social-dot"></div>
      <div class="social-text">Follow us on Chirper<br>@KCPBenefits</div>
    </div>

    <div class="tollfree">
      <div class="tollfree-label">toll free:</div>
      <div class="tollfree-number">800.555.0142</div>
    </div>
  </section>
</body>
</html>
```